Cover for a short novel to be published as an e-book.

I'm looking for an image to use for my e-book cover. It's a short (~42k words) novel/novella that deals humorously with the afterlife and some religious/mythological themes.

I was thinking something that was more graphic design-based rather than illustrative, and it would be awesome if it could somehow convey that it's a light, humorous story.

I plan to self-publish, so the image will end up being fairly small, but it should have some pop to draw people in.

Here's the text for the cover:

A Quiet Hour Before Supper
a novel(la) by Colin Brasby

```html
<!DOCTYPE html>
<html lang="en">
<head>
<meta charset="utf-8">
<title>A Quiet Hour Before Supper — Cover</title>
<link rel="stylesheet" href="https://fonts.googleapis.com/css2?family=Ribeye+Marrow&family=Questrial&family=Kanit:wght@700&display=swap">
<style>
  :root {
    --backdrop: #e4e2df;
    --cover: #f7f8f8;
    --ink: #1b1b1b;
    --accent: #a3182a;
    --accent-dark: #7d0f1d;
  }
  html, body {
    margin: 0;
    width: 1200px;
    height: 1031px;
    overflow: hidden;
    background: var(--backdrop);
  }
  .canvas {
    position: relative;
    width: 1200px;
    height: 1031px;
    display: flex;
    align-items: center;
    justify-content: center;
  }
  .cover {
    position: relative;
    width: 600px;
    height: 960px;
    background: var(--cover);
    box-shadow: 0 10px 30px rgba(0,0,0,0.18);
  }
  .title {
    position: absolute;
    top: 130px;
    left: 0;
    right: 0;
    margin: 0;
    text-align: center;
    font-family: "Ribeye Marrow", serif;
    font-weight: 400;
    text-transform: uppercase;
    color: var(--ink);
    line-height: 1.05;
  }
  .title__line {
    display: block;
    font-size: 48px;
    letter-spacing: -1px;
  }
  .title__key {
    display: block;
    margin-top: 22px;
    font-size: 88px;
    letter-spacing: -3px;
    color: var(--accent);
  }
  .mark-area {
    position: absolute;
    top: 530px;
    left: 165px;
    width: 280px;
    height: 130px;
    border-radius: 6px;
    background: linear-gradient(135deg, var(--accent), var(--accent-dark));
  }
  .byline {
    position: absolute;
    right: 55px;
    bottom: 80px;
    margin: 0;
    font-family: "Questrial", sans-serif;
    font-size: 28px;
    color: var(--ink);
    letter-spacing: 1px;
  }
  .byline__author {
    font-family: "Kanit", sans-serif;
    font-weight: 700;
    font-size: 28px;
    letter-spacing: 0.5px;
  }
</style>
</head>
<body>
<main class="canvas">
  <article class="cover">
    <h1 class="title">
      <span class="title__line">A</span>
      <span class="title__line">Quiet</span>
      <span class="title__line">Hour</span>
      <span class="title__line">Before</span>
      <span class="title__key">Supper</span>
    </h1>

    <div class="mark-area" role="img" aria-label="Two red crossed-bar marks, like closed eyes, sit here"></div>

    <p class="byline">a novel(la) by <span class="byline__author">Colin Brasby</span></p>
  </article>
</main>
</body>
</html>
```